Event Invitation Design for Finance Industry

PLVE www.plve.org.au
We need a online invitation/poster design for our up coming event.
In the attached documents you will find:
= PLVE Main Logo (must be displayed in the top half of the invite)
= A Background image (maybe display this at the bottom of the invite and extend the dark sky upwards as a background for the content/text)
= An example of last years invite (we want a better design then that but similar layout)
= All of our sponsors logos (which need to displayed at the bottom of the invite)
Color: Use the attached example for color ideas.
Dimensions: A4 size. We will NOT be creating a printed copy, it will only be used as an online invite (see attached example for rough dimensions) so the TEXT MOST BY BIG AND SHOULD BE EASILY READABLE FROM PC SCREEN (invite will be displayed online)
-------Below is the text and content for the invite/poster:-------
PLVE Futures Industry Evening
Join fellow industry professionals for an evening of socialising, drinks and appetisers. This event is co-sponsored by PLVE, Dorrington Bank, Vantor Systems, Halbeck Corwin, BQL and OVADI
There will be a Lucky Door Prize, Raffle and Silent Auction with all proceeds being donated to the Pelling Children's Hospital Foundation.
Please RSVP to confirm you will be attending.
Date:
24th July 2014
Time:
6:00 p.m. - 9:00 p.m. AEST
Location:
Brisa Tolley
7 Corvane Pier
North Promenade
Tolverne NSW 2188
Australia
Financial industry professionals
Industry

```html
<!DOCTYPE html>
<html lang="en">
<head>
<meta charset="utf-8">
<title>PLVE Futures Industry Evening</title>
<link rel="stylesheet" href="https://fonts.googleapis.com/css2?family=Source+Sans+3:wght@400;600;700&display=swap">
<style>
  :root {
    --page: #eef1f4;
    --sky-top: #0d0f24;
    --sky-mid: #171a3a;
    --sky-low: #1c2044;
    --band: #2f86cf;
    --ink-navy: #0f1a33;
    --gold: #f4c56a;
    --white: #ffffff;
    --sponsor-ink: #1d2b4a;
    --sponsor-blue: #2b7cc4;
  }
  * { box-sizing: border-box; margin: 0; padding: 0; }
  html, body { width: 1200px; height: 848px; overflow: hidden; }
  body {
    background: var(--page);
    font-family: "Source Sans 3", "Myriad Pro", sans-serif;
    position: relative;
  }
  .invite {
    position: absolute;
    left: 317px; top: 34px;
    width: 600px; height: 776px;
    overflow: hidden;
    box-shadow: 0 2px 6px rgba(0,0,0,.25);
    background:
      radial-gradient(circle at 460px 150px, rgba(255,255,255,.85) 0, rgba(190,225,255,.35) 30px, rgba(120,180,240,0) 110px),
      linear-gradient(180deg, var(--sky-top) 0%, var(--sky-mid) 50%, var(--sky-low) 88%);
  }
  .brand-tab {
    position: absolute; left: 34px; top: 0;
    width: 131px; height: 128px;
    background: var(--white);
    display: flex; align-items: center; justify-content: center; gap: 8px;
    z-index: 3;
  }
  .brand-tab .dot {
    width: 18px; height: 18px; border-radius: 50%;
    background: var(--band);
  }
  .brand-tab .name {
    font-size: 36px; font-weight: 700; color: var(--ink-navy); letter-spacing: 1px;
  }
  .band {
    position: absolute; left: 0; top: 78px; width: 600px; height: 204px; z-index: 1;
  }
  .title {
    position: absolute; left: 30px; top: 142px; z-index: 2;
    font-size: 52px; font-weight: 600; color: var(--white);
    letter-spacing: -.5px; line-height: 1;
    text-shadow: 0 1px 3px rgba(0,0,0,.3);
  }
  .intro {
    position: absolute; left: 30px; top: 205px; width: 545px; z-index: 2;
    font-size: 15.5px; font-weight: 700; color: var(--ink-navy); line-height: 21.5px;
  }
  .charity {
    position: absolute; left: 30px; top: 331px; width: 555px;
    font-size: 17.5px; font-weight: 600; color: var(--gold); line-height: 22px;
  }
  .marker {
    position: absolute; left: 0; top: 389px;
    width: 0; height: 0;
    border-top: 17px solid transparent;
    border-bottom: 17px solid transparent;
    border-left: 19px solid var(--gold);
  }
  .details {
    position: absolute; left: 30px; top: 394px;
    color: var(--white); font-size: 15.5px; font-weight: 600; line-height: 20.5px;
    border-collapse: collapse;
  }
  .details td { vertical-align: top; padding-bottom: 6px; }
  .details .label { width: 66px; }
  .details .sep { width: 18px; }
  .venue-photo {
    position: absolute; left: 0; top: 530px; width: 600px; height: 154px;
    background:
      linear-gradient(180deg, rgba(28,32,68,0) 0%, rgba(60,52,50,.75) 35%, #6b4e2e 60%, #3a3a48 100%);
  }
  .rsvp {
    position: absolute; left: 34px; top: 655px;
    color: var(--white); font-size: 17.5px; font-weight: 600;
  }
  .rsvp-button {
    position: absolute; left: 431px; top: 652px; width: 138px; height: 32px;
    background: var(--band); color: var(--white);
    border-radius: 8px 8px 0 0;
    font-size: 18px; font-weight: 700;
    display: flex; align-items: center; justify-content: center;
    text-decoration: none;
  }
  .sponsors {
    position: absolute; left: 0; top: 684px; width: 600px; height: 92px;
    background: var(--white);
  }
  .sponsors h2 {
    position: absolute; left: 34px; top: 7px;
    font-size: 11.5px; font-weight: 700; color: #111;
  }
  .sponsor-row {
    position: absolute; left: 0; top: 30px; width: 600px; height: 52px;
    list-style: none;
  }
  .sponsor {
    position: absolute; top: 0; height: 52px; transform: translateX(-50%);
    display: flex; align-items: center; gap: 6px;
    font-weight: 700; color: var(--sponsor-ink); white-space: nowrap;
  }
  .sponsor .sq { width: 14px; height: 14px; background: var(--sponsor-ink); }
  .sponsor .ci { width: 14px; height: 14px; border-radius: 50%; background: var(--sponsor-blue); }
  .s-dorrington { left: 61px; font-size: 12px; }
  .s-vantor { left: 182px; font-size: 13px; color: var(--sponsor-blue); }
  .s-halbeck { left: 306px; font-size: 12px; color: #555; }
  .s-ovadi { left: 431px; font-size: 20px; }
  .s-bql { left: 544px; font-size: 18px; }
</style>
</head>
<body>
  <article class="invite">
    <div class="brand-tab"><span class="dot"></span><span class="name">PLVE</span></div>

    <svg class="band" viewBox="0 0 600 204" aria-hidden="true">
      <polygon fill="var(--band)" points="0,22 30,18 60,26 95,16 120,24 150,20 175,28 205,14 240,22 270,12 300,20 330,10 360,16 395,6 420,14 450,4 480,10 510,2 545,8 575,0 600,4 600,172 570,178 540,168 510,180 480,170 450,186 420,174 390,190 360,178 330,194 300,182 270,198 240,186 210,200 180,188 150,202 120,190 90,200 60,186 30,196 0,184"/>
    </svg>

    <h1 class="title">Futures Industry Evening</h1>
    <p class="intro">Join fellow industry professionals for an evening of socialising, drinks and appetisers. This event is co-sponsored by PLVE, Dorrington Bank, Vantor Systems, Halbeck Corwin, BQL and OVADI.</p>

    <p class="charity">There will be a Lucky Door Prize, Raffle and Silent Auction with all proceeds being donated to the Pelling Children's Hospital Foundation.</p>

    <span class="marker"></span>
    <table class="details">
      <tr><td class="label">Date</td><td class="sep">:</td><td>24th July 2014</td></tr>
      <tr><td class="label">Time</td><td class="sep">:</td><td>6:00 p.m. - 9:00 p.m. AEST</td></tr>
      <tr><td class="label">Location</td><td class="sep">:</td><td>Brisa Tolley, 7 Corvane Pier<br>North Promenade<br>Tolverne NSW 2188<br>Australia</td></tr>
    </table>

    <div class="venue-photo" role="img" aria-label="Night view of the waterfront venue on the pier, lit with warm lights"></div>

    <p class="rsvp">Please RSVP to confirm you will be attending.</p>
    <a class="rsvp-button" href="#rsvp">CLICK HERE!</a>

    <footer class="sponsors">
      <h2>Sponsored by:</h2>
      <ul class="sponsor-row">
        <li class="sponsor s-dorrington"><span class="sq"></span>Dorrington Bank</li>
        <li class="sponsor s-vantor">Vantor Systems</li>
        <li class="sponsor s-halbeck">Halbeck Corwin</li>
        <li class="sponsor s-ovadi">OVADI</li>
        <li class="sponsor s-bql"><span class="ci"></span>BQL</li>
      </ul>
    </footer>
  </article>
</body>
</html>
```